Design a label for a range of honey under :BRIGHT MEADOW HONEY. (Original quirky different)

Create a label for a range of honey products under the brand BRIGHT MEADOW HONEY.
Iam the beekeeper and want to sell for the local New Zealand market directly to the consumer, online mainly.
Brand position: A contemporary honey, a fresh look for a simple product, like nature intended, nothing taken out, nothing added. Doesnt take itself seriously.
Personality: Contemporary, fresh, modern, free and fun,loving. Doesnt take itself seriously, loving, generous, upbeat, provide enjoyment, life ...
Brand value: Straight up, keep it simple, generous, different,
Label: Modern twist of nature and goodness (no straight picture of nature) quirky?, use of slogan? ( Nature in a pot / More than just honey / Taste of nature / It's all good...
Need to stand out, make you smile, be noticed, different...

Target Market(s)

Online direct customer.

Requirements
Must have
• legal requirements for NZ labeling attached.
A twist and quirky side...
Should not have
• Basic picture of nature.
Straight forward boring everybody else's feel.

```html
<!DOCTYPE html>
<html lang="en">
<head>
<meta charset="utf-8">
<title>Bright Meadow Honey – Label Range</title>
<link rel="stylesheet" href="https://fonts.googleapis.com/css2?family=Amatic+SC:wght@700&family=PT+Sans:wght@400;700&display=swap">
<style>
  :root {
    --page: #ffffff;
    --ink: #231f20;
    --white: #ffffff;
    --sky: #45a6cc;
    --marigold: #f6981f;
    --olive: #9a8428;
    --fern-tone: rgba(255, 255, 255, 0.85);
  }
  * { margin: 0; padding: 0; box-sizing: border-box; }
  html, body {
    width: 1200px;
    height: 666px;
    overflow: hidden;
    background: var(--page);
  }
  .range {
    position: relative;
    width: 1200px;
    height: 666px;
  }
  .label {
    position: absolute;
    width: 246px;
    height: 255px;
    border-radius: 16px;
    color: var(--white);
    font-family: "PT Sans", sans-serif;
    transform-origin: top left;
  }
  .label--sky { left: 151px; top: 385px; background: var(--sky); transform: scale(0.716); }
  .label--marigold { left: 445px; top: 283px; background: var(--marigold); }
  .label--olive { left: 817px; top: 283px; background: var(--olive); }

  .brand-name {
    position: absolute;
    left: 0;
    top: 24px;
    width: 100%;
    text-align: center;
    font-family: "PT Sans", sans-serif;
    font-weight: 700;
    font-size: 17px;
    line-height: 22px;
    color: var(--ink);
    letter-spacing: 0.5px;
  }
  .fern-sprig {
    position: absolute;
    left: 40px;
    top: 56px;
    width: 40px;
    height: 92px;
    border-radius: 50% 50% 40% 40%;
    background: var(--fern-tone);
    opacity: 0.9;
    transform: rotate(-18deg);
  }
  .natural-tag {
    position: absolute;
    left: 166px;
    top: 86px;
    font-family: "Amatic SC", sans-serif;
    font-weight: 700;
    color: var(--white);
    text-align: center;
    line-height: 0.9;
    transform: rotate(-14deg);
  }
  .natural-tag__pct { display: block; font-size: 26px; }
  .natural-tag__word { display: block; font-size: 14px; letter-spacing: 0.5px; }
  .product-name {
    position: absolute;
    left: 0;
    top: 148px;
    width: 100%;
    text-align: center;
    font-family: "Amatic SC", sans-serif;
    font-weight: 700;
    font-size: 60px;
    line-height: 1;
    letter-spacing: 6px;
    text-indent: 6px;
  }
  .producer {
    position: absolute;
    left: 0;
    top: 205px;
    width: 100%;
    text-align: center;
    color: var(--ink);
    font-size: 9px;
    line-height: 11px;
  }
  .volume {
    position: absolute;
    left: 0;
    top: 233px;
    width: 100%;
    text-align: center;
    color: var(--ink);
    font-size: 12px;
  }
</style>
</head>
<body>
<main class="range">

  <section class="label label--sky">
    <h1 class="brand-name">BRIGHT MEADOW HONEY</h1>
    <div class="fern-sprig" role="img" aria-label="White fern sprig illustration"></div>
    <p class="natural-tag"><span class="natural-tag__pct">100%</span><span class="natural-tag__word">NATURAL</span></p>
    <h2 class="product-name">HONEY</h2>
    <p class="producer">Clover Hill Apiary Ltd.<br>48 Kowhai Lane, Nelson, NZ</p>
    <p class="volume">500 ml</p>
  </section>

  <section class="label label--marigold">
    <h1 class="brand-name">BRIGHT MEADOW HONEY</h1>
    <div class="fern-sprig" role="img" aria-label="White fern sprig illustration"></div>
    <p class="natural-tag"><span class="natural-tag__pct">100%</span><span class="natural-tag__word">NATURAL</span></p>
    <h2 class="product-name">HONEY</h2>
    <p class="producer">Clover Hill Apiary Ltd.<br>48 Kowhai Lane, Nelson, NZ</p>
    <p class="volume">500 ml</p>
  </section>

  <section class="label label--olive">
    <h1 class="brand-name">BRIGHT MEADOW HONEY</h1>
    <div class="fern-sprig" role="img" aria-label="White fern sprig illustration"></div>
    <p class="natural-tag"><span class="natural-tag__pct">100%</span><span class="natural-tag__word">NATURAL</span></p>
    <h2 class="product-name">HONEY</h2>
    <p class="producer">Clover Hill Apiary Ltd.<br>48 Kowhai Lane, Nelson, NZ</p>
    <p class="volume">500 ml</p>
  </section>

</main>
</body>
</html>
```